High End Business Card Design for Flooring Store

Looking for a new card design for our hardwood flooring company. We have no print budget for these and are open to cards made from wood, metal, cardstock with embossed print ... or any combination of these. No plastic.

We sell luxury products and I want the cards to reflect our image of quality and class.

Our contact information as such;
Employee Name
418 Colbrook Blvd.
Ashgrove, ON
K9R-3M5
(555) 214-3968
Employee email @velkaflooring.com

Target Market(s)

Home Builders

Contact Information for Business Card

Emnployee name, business contact information

```html
<!DOCTYPE html>
<html lang="en">
<head>
<meta charset="utf-8">
<title>Velka Flooring & Stairs – Business Card</title>
<link rel="stylesheet" href="https://fonts.googleapis.com/css2?family=Montserrat:wght@500;600&family=Outfit:wght@400;500;700&display=swap">
<style>
  :root {
    --stage: #6d7174;
    --card-dark: #1f1f1f;
    --card-light: #ffffff;
    --brand-red: #9a2a24;
    --brand-gold: #e8b42c;
    --ink: #222222;
    --rule: #7a7a7a;
  }
  * { margin: 0; padding: 0; box-sizing: border-box; }
  html, body { width: 1200px; height: 1200px; overflow: hidden; }
  body { background: var(--stage); position: relative; font-family: "Outfit", sans-serif; }

  .card { position: absolute; left: 245px; width: 710px; height: 410px; }
  .card-front { top: 130px; background: var(--card-dark); }
  .card-back { top: 644px; background: var(--card-light); }

  .brand-mark { position: absolute; background: var(--brand-gold); }
  .brand-name {
    position: absolute; font-family: "Montserrat", sans-serif; font-weight: 500;
    color: var(--brand-red); line-height: 1; letter-spacing: 1px;
  }
  .tagline {
    position: absolute; font-family: "Montserrat", sans-serif; font-weight: 500;
    text-align: center; line-height: 1; white-space: nowrap;
  }

  .card-front .brand-mark { left: 190px; top: 150px; width: 52px; height: 52px; }
  .card-front .brand-name { left: 256px; top: 128px; font-size: 96px; }
  .card-front .tagline { left: 10px; width: 100%; color: #fff; font-size: 24px; }
  .card-front .tagline-fr { top: 224px; }
  .card-front .tagline-en { top: 249px; }

  .card-back .brand-mark { left: 106px; top: 180px; width: 30px; height: 30px; }
  .card-back .brand-name { left: 144px; top: 166px; font-size: 54px; }
  .card-back .tagline { left: 120px; width: 200px; color: var(--ink); font-size: 13px; }
  .card-back .tagline-fr { top: 224px; }
  .card-back .tagline-en { top: 239px; }

  .divider { position: absolute; left: 340px; top: 116px; width: 1px; height: 183px; background: var(--rule); }

  .person-name { position: absolute; left: 369px; top: 122px; font-size: 24px; line-height: 1; font-weight: 700; color: var(--brand-red); letter-spacing: 1.2px; }
  .person-role { position: absolute; left: 370px; top: 151px; font-size: 16px; line-height: 1; color: var(--ink); }

  .contact-list { position: absolute; left: 368px; top: 184px; list-style: none; color: var(--ink); font-size: 16px; }
  .contact-list li { position: relative; padding-left: 28px; height: 24.5px; line-height: 20px; white-space: nowrap; }
  .contact-list li.address { height: auto; line-height: 21px; }
  .contact-list svg { position: absolute; left: 0; top: 3px; width: 14px; height: 14px; fill: var(--brand-red); }

  .accent-band { position: absolute; left: 0; bottom: 0; width: 100%; height: 8px; background: var(--brand-red); }
</style>
</head>
<body>

  <section class="card card-front">
    <span class="brand-mark"></span>
    <span class="brand-name">Velka</span>
    <p class="tagline tagline-fr">Planchers &amp; Escaliers</p>
    <p class="tagline tagline-en">Flooring &amp; Stairs</p>
  </section>

  <section class="card card-back">
    <span class="brand-mark"></span>
    <span class="brand-name">Velka</span>
    <p class="tagline tagline-fr">Planchers &amp; Escaliers</p>
    <p class="tagline tagline-en">Flooring &amp; Stairs</p>

    <span class="divider"></span>

    <h1 class="person-name">Julien Arsenault</h1>
    <p class="person-role">Manager</p>

    <ul class="contact-list">
      <li>
        <svg viewBox="0 0 14 14" aria-hidden="true"><path d="M4 1 L6 1 L6.5 4 L5 5 Q6 8 8.5 9.5 L9.5 8 L12.5 8.5 L12.5 10.5 Q12 13 9 12.5 Q2.5 10.5 1.5 4 Q1.5 1.5 4 1 Z"/></svg>
        (555)214-3968
      </li>
      <li>
        <svg viewBox="0 0 14 14" aria-hidden="true"><path d="M0 3 H14 V11 H0 Z M1 3.8 L7 8 L13 3.8 V4.8 L7 9 L1 4.8 Z" fill-rule="evenodd"/></svg>
        Info@velkaflooring.com
      </li>
      <li>
        <svg viewBox="0 0 14 14" aria-hidden="true"><circle cx="7" cy="7" r="6" fill="none" stroke="#9a2a24" stroke-width="1.4"/><path d="M1 7 H13 M7 1 V13" stroke="#9a2a24" stroke-width="1.2"/></svg>
        www.velkaflooring.com
      </li>
      <li class="address">
        <svg viewBox="0 0 14 14" aria-hidden="true"><path d="M7 0.5 A5 5 0 0 1 12 5.5 Q12 9 7 13.5 Q2 9 2 5.5 A5 5 0 0 1 7 0.5 Z M7 3.5 A2 2 0 1 0 7 7.5 A2 2 0 1 0 7 3.5 Z" fill-rule="evenodd"/></svg>
        418 Colbrook Blvd.<br>Ashgrove, ON K9R 3M5
      </li>
    </ul>

    <span class="accent-band"></span>
  </section>

</body>
</html>
```